RESIDENCE VALBRUNETTE

The CORVALIS Immobilier company exclusively offers apartments for sale under a tax exemption law (BRESSAUTINIÉ) in CAMBRAI, 92 apartments are available, fully renovated with balcony, terrace, elevator, in a former military residence known to the city.
We want to make a book to give to our customers.

```html
<!DOCTYPE html>
<html lang="fr">
<head>
<meta charset="utf-8">
<title>Résidence Valbrunette — Livret acquéreurs</title>
<link rel="stylesheet" href="https://fonts.googleapis.com/css2?family=EB+Garamond:wght@400;500&family=Nunito:wght@400;700;800&display=swap">
<style>
  :root{
    --bg:#000;
    --paper:#fff;
    --ink:#222;
    --muted:#777;
    --gold:#b79a68;
    --gold-title:#bfa06c;
    --tan:#b8a483;
    --tan-line:#d8cbb4;
    --plan:#eeece8;
    --fold:#d9d9d9;
    --serif:'EB Garamond', Georgia, serif;
    --sans:'Nunito', Arial, sans-serif;
  }
  *{box-sizing:border-box;margin:0;padding:0}
  html,body{width:734px;height:1200px;overflow:hidden;background:var(--bg)}
  body{position:relative;font-family:var(--serif);color:var(--ink)}

  .spread{position:absolute;left:69px;width:596px;height:210px;display:flex}
  .page{position:relative;width:298px;height:210px;background:var(--paper);overflow:hidden}
  .page + .page{border-left:1px solid var(--fold)}

  .folio{position:absolute;bottom:6px;font-family:var(--serif);font-size:3px;font-weight:500;letter-spacing:.1px;text-transform:uppercase;white-space:nowrap}
  .folio--left{left:12px}
  .folio--right{right:12px}

  .visual{position:absolute}
  .visual--aerial{background:linear-gradient(180deg,#9ec3dd 0%,#c6d6dc 22%,#b5613f 34%,#c98a6c 50%,#7f9a58 70%,#6f8f4a 100%)}
  .visual--facade{background:linear-gradient(100deg,#c9d7e3 0%,#b25c3e 30%,#a6553a 60%,#c9c4bb 85%,#9aa66a 100%)}
  .visual--plan{background:var(--plan);border:1px solid #ddd}
  .visual--plan3d{background:linear-gradient(135deg,#e6e2dc 0%,#c98a52 35%,#d39a5f 55%,#6f8a92 75%,#e9e5df 100%)}
  .visual--interior{background:linear-gradient(180deg,#dcdad6 0%,#c7c3bb 45%,#8e6a48 75%,#a27a52 100%)}
  .visual--lounge{background:linear-gradient(180deg,#e3e1dc 0%,#b6b9b3 45%,#4f6a64 70%,#8b6a4a 100%)}
  .visual--press{background:linear-gradient(180deg,#c9d7e2 0%,#b56f52 45%,#8d9a6a 100%)}

  .caption{position:absolute;font-family:var(--sans);font-size:2.6px;color:var(--muted);white-space:nowrap}

  .lede{position:absolute;font-size:3.4px;line-height:1.3;text-align:justify}
  .notice{position:absolute;font-size:3.2px;line-height:1.5}
  .notice p{margin-bottom:4px}
  .notice .caps{text-transform:uppercase}

  .conditions-icon{position:absolute;left:35px;top:84px;width:38px;height:38px}
  .conditions-title{position:absolute;left:87px;top:80px;font-size:10px;font-weight:400}
  .conditions-text{position:absolute;left:87px;top:98px;width:160px;font-size:3.2px;line-height:1.35}

  .apt-kicker{position:absolute;font-family:var(--sans);font-size:2.6px;line-height:1.3;color:var(--muted)}
  .apt-name{position:absolute;font-family:var(--sans);font-weight:800;font-size:14px;color:var(--gold-title);letter-spacing:.2px;white-space:nowrap}
  .apt-type{position:absolute;font-family:var(--sans);font-size:4px;color:var(--gold-title);white-space:nowrap}
  .apt-table{position:absolute;background:var(--tan);padding:4px 6px;color:#fff;font-family:var(--sans)}
  .apt-table h3{font-size:2.6px;font-weight:400;line-height:1.3;margin-bottom:3px}
  .apt-table .row{display:flex;justify-content:space-between;font-size:2.3px;line-height:1;padding:.6px 0;border-bottom:.4px solid var(--tan-line)}
  .apt-table .row--total{margin-top:3px}
  .apt-note{position:absolute;left:18px;bottom:18px;width:210px;font-family:var(--sans);font-size:2.2px;line-height:1.3;color:var(--muted)}
  .partner{position:absolute;text-align:center;font-family:var(--sans);font-weight:700;font-size:5px;color:var(--ink);line-height:1.2;white-space:nowrap}
  .partner small{display:block;font-size:2.4px;font-weight:400;letter-spacing:1px;color:var(--gold)}

  .brand{position:absolute;left:0;top:88px;width:192px;text-align:center;font-family:var(--sans);font-weight:700;color:var(--gold);font-size:16px;letter-spacing:2px;line-height:1.1}
  .brand span{display:block;font-size:7px;letter-spacing:4.5px}
  .press{position:absolute;left:192px;top:12px;width:95px;height:186px;border:.5px solid #bbb;padding:3px;font-family:Arial,sans-serif;overflow:hidden}
  .press h2{font-size:5px;font-weight:700;line-height:1.15;margin-bottom:2px}
  .press .intro{font-size:2.2px;font-weight:700;line-height:1.2;margin-bottom:2px}
  .press .cols{columns:2;column-gap:3px;font-size:2px;line-height:1.25;text-align:justify}
  .press .cols p{margin-bottom:2px}
</style>
</head>
<body>

<section class="spread" style="top:123px">
  <article class="page">
    <div class="visual visual--aerial" role="img" aria-label="Vue aérienne de la résidence Valbrunette, bâtiments en brique et jardin central" style="left:13px;top:23px;width:202px;height:114px"></div>
    <p class="lede" style="left:196px;top:151px;width:90px">La Résidence Valbrunette offre un cadre de vie calme au cœur de Cambrai. Ses 92 appartements entièrement rénovés disposent de balcons, terrasses et ascenseurs. Ancienne résidence militaire bien connue des habitants, elle allie charme historique et confort moderne pour un investissement serein et durable.</p>
    <div class="folio folio--right">Corvalis Immobilier // 11</div>
  </article>
  <article class="page">
    <div class="visual visual--facade" role="img" aria-label="Façade en brique d'un immeuble rénové de la résidence" style="left:0;top:0;width:82px;height:210px"></div>
    <div class="notice" style="left:86px;top:30px;width:200px">
      <p>Investir en toute sécurité<br>Conseils pour investir en loi Bressautinié<br>Perte du bénéfice de la réduction d'impôt : logement non loué<br>Passage notaire en n+1 : hausse des taux d'emprunt<br>la-loi-bressautinie.net</p>
      <p class="caps" style="margin-top:28px">Afin de parer à ces risques éventuels</p>
      <p>Faites-vous aider par un professionnel : prenez rendez-vous gratuitement et sans engagement au 01 40 00 12 34.</p>
      <p>Nous vous accueillons dans nos bureaux au 8, rue des Tanneurs - 75002 Paris. Un conseiller se déplace chez vous. Un conseiller vous appelle pour discuter ensemble de votre projet.</p>
      <p style="margin-top:14px">Nos conseillers sont à votre disposition du lundi au vendredi de 9h à 19h*<br>*Nos conseillers peuvent également vous accueillir le samedi de 10h à 15h si nécessaire</p>
    </div>
    <div class="folio folio--right">Corvalis Immobilier // 13</div>
  </article>
</section>

<section class="spread" style="top:345px">
  <article class="page">
    <svg class="conditions-icon" viewBox="0 0 38 38" aria-hidden="true">
      <circle cx="19" cy="19" r="17.5" fill="none" stroke="#333" stroke-width="1.3"/>
      <circle cx="19" cy="11" r="2" fill="#333"/>
      <path d="M16 16h4v12h2.5v1.5h-8V28H17v-10.5h-1z" fill="#333"/>
    </svg>
    <h2 class="conditions-title">Les conditions à respecter</h2>
    <p class="conditions-text">Aucune reprise de l'avantage fiscal acquis n'est effectuée en cas d'invalidité correspondant au classement dans la deuxième ou la troisième des catégories prévues à l'article L. 341-4 du code de la sécurité sociale, de licenciement ou de décès du contribuable ou de l'un des membres du couple soumis à imposition commune.</p>
    <div class="folio folio--left">Corvalis Immobilier // 12</div>
  </article>
  <article class="page">
    <p class="apt-kicker" style="left:18px;top:31px">Rénovation de 3 immeubles d'habitation<br>Rue des Valbrunes - Cambrai<br>Avril 2022</p>
    <h2 class="apt-name" style="left:25px;top:52px">Margaux</h2>
    <p class="apt-type" style="left:25px;top:72px">Appartement T4 - 76,90 m²</p>
    <div class="apt-table" style="left:19px;top:101px;width:84px;height:39px">
      <h3>Appartement MARGAUX<br>Bât. B - 1er étage - T4</h3>
      <div class="row"><span>Séjour cuisine</span><span>31,60 m²</span></div>
      <div class="row"><span>Chambre 1</span><span>11,20 m²</span></div>
      <div class="row"><span>Chambre 2</span><span>10,80 m²</span></div>
      <div class="row"><span>Chambre 3</span><span>9,60 m²</span></div>
      <div class="row row--total"><span>Surface habitable</span><span>76,90 m²</span></div>
    </div>
    <div class="visual visual--plan" role="img" aria-label="Plan de l'appartement Margaux" style="left:116px;top:31px;width:58px;height:60px"></div>
    <p class="caption" style="left:116px;top:93px">Plan de l'appartement</p>
    <div class="visual visual--interior" role="img" aria-label="Vue intérieure du séjour et de la cuisine" style="left:200px;top:31px;width:82px;height:60px"></div>
    <div class="visual visual--plan3d" role="img" aria-label="Vue 3D meublée de l'appartement Margaux" style="left:119px;top:99px;width:64px;height:52px"></div>
    <p class="caption" style="left:119px;top:153px">Vue 3D de l'appartement</p>
    <div class="visual visual--lounge" role="img" aria-label="Vue intérieure du salon" style="left:200px;top:99px;width:82px;height:60px"></div>
    <div class="partner" style="left:228px;top:171px">Atelier Ardent<small>DÉVELOPPEMENT</small></div>
    <p class="apt-note">Nota : document provisoire, sous réserve d'autorisations administratives et de faisabilité technique. Mobilier non contractuel.</p>
    <div class="folio folio--left">Corvalis Immobilier // 14</div>
  </article>
</section>

<section class="spread" style="top:572px">
  <article class="page">
    <p class="apt-kicker" style="left:22px;top:27px">Rénovation de 3 immeubles d'habitation<br>Rue des Valbrunes - Cambrai<br>Avril 2022</p>
    <h2 class="apt-name" style="left:27px;top:47px">Bastien</h2>
    <p class="apt-type" style="left:27px;top:66px">Appartement T3 - 73,80 m²</p>
    <div class="apt-table" style="left:20px;top:98px;width:81px;height:61px">
      <h3>Appartement BASTIEN<br>Bât. A - 2e étage - T3</h3>
      <div class="row"><span>Séjour cuisine</span><span>30,40 m²</span></div>
      <div class="row"><span>Entrée</span><span>6,20 m²</span></div>
      <div class="row"><span>Dégagement</span><span>3,80 m²</span></div>
      <div class="row"><span>Chambre 1</span><span>12,60 m²</span></div>
      <div class="row"><span>Chambre 2</span><span>11,40 m²</span></div>
      <div class="row"><span>Salle d'eau</span><span>5,90 m²</span></div>
      <div class="row"><span>WC</span><span>1,60 m²</span></div>
      <div class="row"><span>Balcon</span><span>4,20 m²</span></div>
      <div class="row row--total"><span>Surface habitable</span><span>73,80 m²</span></div>
    </div>
    <div class="visual visual--plan" role="img" aria-label="Plan de l'appartement Bastien" style="left:122px;top:24px;width:52px;height:59px"></div>
    <p class="caption" style="left:122px;top:85px">Plan de l'appartement</p>
    <div class="visual visual--interior" role="img" aria-label="Vue intérieure depuis le salon" style="left:195px;top:24px;width:82px;height:59px"></div>
    <div class="visual visual--plan3d" role="img" aria-label="Vue 3D meublée de l'appartement Bastien" style="left:122px;top:99px;width:54px;height:52px"></div>
    <p class="caption" style="left:122px;top:153px">Vue 3D de l'appartement</p>
    <div class="visual visual--lounge" role="img" aria-label="Vue intérieure de la cuisine ouverte" style="left:195px;top:99px;width:82px;height:59px"></div>
    <div class="partner" style="left:226px;top:169px">Atelier Ardent<small>DÉVELOPPEMENT</small></div>
    <p class="apt-note">Nota : document provisoire, sous réserve d'autorisations administratives et de faisabilité technique. Mobilier non contractuel.</p>
    <div class="folio folio--right">Corvalis Immobilier // 15</div>
  </article>
  <article class="page">
    <p class="apt-kicker" style="left:22px;top:24px">Rénovation de 3 immeubles d'habitation<br>Rue des Valbrunes - Cambrai<br>Avril 2022</p>
    <h2 class="apt-name" style="left:27px;top:44px">Hélène</h2>
    <p class="apt-type" style="left:27px;top:63px">Appartement T5 duplex - 107,20 m²</p>
    <div class="apt-table" style="left:20px;top:96px;width:82px;height:62px">
      <h3>Appartement HÉLÈNE<br>Bât. C - 3e étage - T5 duplex</h3>
      <div class="row"><span>Séjour cuisine</span><span>36,80 m²</span></div>
      <div class="row"><span>Entrée</span><span>5,40 m²</span></div>
      <div class="row"><span>Chambre 1</span><span>13,20 m²</span></div>
      <div class="row"><span>Chambre 2</span><span>11,60 m²</span></div>
      <div class="row"><span>Chambre 3</span><span>10,90 m²</span></div>
      <div class="row"><span>Chambre 4</span><span>9,80 m²</span></div>
      <div class="row"><span>Salle de bain</span><span>6,40 m²</span></div>
      <div class="row"><span>Salle d'eau</span><span>4,70 m²</span></div>
      <div class="row row--total"><span>Surface habitable</span><span>107,20 m²</span></div>
    </div>
    <div class="visual visual--plan" role="img" aria-label="Plan du niveau bas du duplex Hélène" style="left:108px;top:22px;width:40px;height:58px"></div>
    <div class="visual visual--plan" role="img" aria-label="Plan du niveau haut du duplex Hélène" style="left:150px;top:22px;width:40px;height:58px"></div>
    <p class="caption" style="left:108px;top:82px">Plan de l'appartement - bas / haut du duplex</p>
    <div class="visual visual--lounge" role="img" aria-label="Vue intérieure depuis l'entrée" style="left:197px;top:22px;width:82px;height:62px"></div>
    <div class="visual visual--plan3d" role="img" aria-label="Vue 3D du niveau bas du duplex" style="left:108px;top:97px;width:40px;height:50px"></div>
    <div class="visual visual--plan3d" role="img" aria-label="Vue 3D du niveau haut du duplex" style="left:150px;top:97px;width:40px;height:50px"></div>
    <p class="caption" style="left:130px;top:149px">Vue 3D de l'appartement</p>
    <div class="visual visual--interior" role="img" aria-label="Vue intérieure depuis l'escalier" style="left:197px;top:96px;width:82px;height:62px"></div>
    <div class="partner" style="left:228px;top:169px">Atelier Ardent<small>DÉVELOPPEMENT</small></div>
    <p class="apt-note">Nota : document provisoire, sous réserve d'autorisations administratives et de faisabilité technique. Mobilier non contractuel.</p>
    <div class="folio folio--left">Corvalis Immobilier // 16</div>
  </article>
</section>

<section class="spread" style="top:816px">
  <article class="page">
    <p class="apt-kicker" style="left:20px;top:25px">Rénovation de 3 immeubles d'habitation<br>Rue des Valbrunes - Cambrai<br>Avril 2022</p>
    <h2 class="apt-name" style="left:27px;top:45px">Josiane</h2>
    <p class="apt-type" style="left:27px;top:64px">Appartement T4 - 78,80 m²</p>
    <div class="apt-table" style="left:20px;top:97px;width:82px;height:62px">
      <h3>Appartement JOSIANE<br>Bât. B - 2e étage - T4</h3>
      <div class="row"><span>Séjour cuisine</span><span>32,60 m²</span></div>
      <div class="row"><span>Entrée</span><span>5,80 m²</span></div>
      <div class="row"><span>Dégagement</span><span>3,40 m²</span></div>
      <div class="row"><span>Chambre 1</span><span>12,40 m²</span></div>
      <div class="row"><span>Chambre 2</span><span>10,60 m²</span></div>
      <div class="row"><span>Chambre 3</span><span>9,20 m²</span></div>
      <div class="row"><span>Salle d'eau</span><span>4,80 m²</span></div>
      <div class="row row--total"><span>Surface habitable</span><span>78,80 m²</span></div>
    </div>
    <div class="visual visual--plan" role="img" aria-label="Plan de l'appartement Josiane" style="left:122px;top:22px;width:52px;height:59px"></div>
    <p class="caption" style="left:122px;top:83px">Plan de l'appartement</p>
    <div class="visual visual--interior" role="img" aria-label="Vue intérieure depuis la fenêtre" style="left:196px;top:21px;width:82px;height:62px"></div>
    <div class="visual visual--plan3d" role="img" aria-label="Vue 3D meublée de l'appartement Josiane" style="left:124px;top:97px;width:54px;height:52px"></div>
    <p class="caption" style="left:124px;top:151px">Vue 3D de l'appartement</p>
    <div class="visual visual--lounge" role="img" aria-label="Vue intérieure du salon et de la cuisine" style="left:196px;top:97px;width:82px;height:62px"></div>
    <div class="partner" style="left:226px;top:169px">Atelier Ardent<small>DÉVELOPPEMENT</small></div>
    <p class="apt-note">Nota : document provisoire, sous réserve d'autorisations administratives et de faisabilité technique. Mobilier non contractuel.</p>
    <div class="folio folio--right">Corvalis Immobilier // 17</div>
  </article>
  <article class="page">
    <div class="brand">CORVALIS<span>IMMOBILIER</span></div>
    <div class="press">
      <h2>La résidence Valbrunette à CAMBRAI devient la résidence BELVÉDÈRE</h2>
      <p class="intro">Le groupe Corvalis Immobilier vous propose de réaliser un investissement locatif en loi Bressautinié, avec un programme rénové de grande qualité au cœur de Cambrai.</p>
      <div class="visual visual--press" role="img" aria-label="Photographie de la résidence rénovée" style="position:relative;width:100%;height:44px;margin-bottom:3px"></div>
      <div class="cols">
        <p>L'ancienne résidence militaire, bien connue des Cambrésiens, a été entièrement rénovée. Les 92 appartements, du T2 au T5, bénéficient de balcons, terrasses et ascenseurs.</p>
        <p>Cette opération s'inscrit dans le dispositif Bressautinié, qui permet de réduire l'impôt sur le revenu en contrepartie d'une mise en location du logement pendant plusieurs années.</p>
        <p>Les travaux, menés avec un maître d'œuvre local, respectent l'architecture de brique d'origine tout en offrant les normes actuelles d'isolation et de confort.</p>
        <p>Une réelle opportunité : les logements sont proposés à des prix maîtrisés, avec un accompagnement complet, du financement à la gestion locative.</p>
        <p>Les premiers acquéreurs ont déjà choisi leur lot. Les visites sont organisées sur rendez-vous, en semaine comme le samedi.</p>
        <p>Groupe Corvalis Immobilier<br>8, rue des Tanneurs<br>75002 Paris<br>01 40 00 12 34</p>
      </div>
    </div>
    <div class="folio folio--left">Corvalis Immobilier // 18</div>
  </article>
</section>

</body>
</html>
```